Business Card Design

Please see my website www.qvlearnix.com.au to for further information on my services and styling of my site

Reason: Deadline is extended to permit alterations to current designs or for any new submissions. Cheers

Industry/Entity Type

Business

Contact Information for Business Card

Marcus Pelton
Empowerment Coach

'Live your passion'

marcus@qvlearnix.com.au
0438157264
qvlearnix.com.au

```html
<!DOCTYPE html>
<html lang="en">
<head>
<meta charset="utf-8">
<title>QV Learnix Training – Business Card</title>
<link rel="stylesheet" href="https://fonts.googleapis.com/css2?family=Open+Sans:ital,wght@0,400;0,600;0,700;1,400&display=swap">
<style>
  :root {
    --frame: #9a9a9a;
    --card-edge: #8c8c8c;
    --ink: #111111;
    --ink-soft: #555555;
    --lime: #b5d63d;
    --forest: #5b8a3d;
    --mist: #edf2da;
    --shadow-grey: #ececec;
    --white: #ffffff;
  }
  * { margin: 0; padding: 0; box-sizing: border-box; }
  html, body { width: 1200px; height: 1001px; overflow: hidden; background: var(--white); }
  body { font-family: "Open Sans", Arial, sans-serif; color: var(--ink); }
  .canvas {
    position: relative; width: 1200px; height: 1001px;
    border: 1px solid var(--frame); background: var(--white);
  }
  .card {
    position: absolute; top: 378px; width: 422px; height: 261px;
    border: 1px solid var(--card-edge); background: var(--white); overflow: hidden;
  }
  .card--front { left: 135px; }
  .card--back { left: 661px; }

  .card__art { position: absolute; inset: 0; }

  .identity { position: absolute; left: 41px; top: 40px; line-height: 17px; }
  .identity__name { font-size: 14px; font-weight: 700; }
  .identity__role { font-size: 12.5px; }
  .identity__motto { font-size: 12.5px; font-style: italic; }

  .contacts { position: absolute; left: 24px; top: 167px; list-style: none; }
  .contacts__item { display: flex; align-items: center; height: 24px; font-size: 13.5px; }
  .contacts__icon { width: 13px; height: 13px; margin-right: 8px; flex: none; }

  .brand-mark {
    position: absolute; display: flex; align-items: center; gap: 6px;
    font-weight: 600; white-space: nowrap;
  }
  .brand-mark__dot { width: 9px; height: 9px; border-radius: 50%; flex: none; }
  .card--front .brand-mark { left: 264px; top: 207px; color: var(--white); font-size: 14px; }
  .card--front .brand-mark__dot { background: var(--white); }
  .card--back .brand-mark { left: 0; right: 0; justify-content: center; top: 94px; color: var(--lime); font-size: 14px; }
  .card--back .brand-mark__dot { background: var(--lime); }

  .services {
    position: absolute; top: 143px; left: 0; right: 0;
    display: flex; justify-content: center; font-size: 11px; line-height: 14px; color: var(--ink-soft);
  }
  .services__item { padding: 0 7px; }
  .services__item--left { text-align: right; border-right: 1px solid var(--ink-soft); }
  .services__title { font-weight: 700; }

  .back-contacts {
    position: absolute; top: 215px; left: 98px;
    display: flex; gap: 26px; font-size: 11px; font-weight: 700; color: var(--ink-soft);
  }
</style>
</head>
<body>
<main class="canvas">

  <section class="card card--front" aria-label="Business card front">
    <svg class="card__art" width="422" height="261" viewBox="0 0 422 261">
      <defs>
        <linearGradient id="swoosh" x1="0" y1="0" x2="0" y2="1">
          <stop offset="0" stop-color="#b5d63d"/>
          <stop offset="0.45" stop-color="#7ea93f"/>
          <stop offset="1" stop-color="#5b8a3d"/>
        </linearGradient>
        <linearGradient id="figures" x1="0" y1="0" x2="0" y2="1">
          <stop offset="0" stop-color="#edf2da"/>
          <stop offset="1" stop-color="#ececec"/>
        </linearGradient>
      </defs>
      <rect x="145" y="22" width="190" height="239" rx="40" fill="url(#figures)" role="img" aria-label="Faint silhouettes of people raising their arms"/>
      <path d="M85 261 C 220 240, 330 180, 422 54 L 422 261 Z" fill="url(#swoosh)"/>
    </svg>

    <div class="identity">
      <p class="identity__name">Marcus Pelton</p>
      <p class="identity__role">Empowerment Coach</p>
      <p class="identity__motto">'Live your passion'</p>
    </div>

    <ul class="contacts">
      <li class="contacts__item">
        <svg class="contacts__icon" viewBox="0 0 13 13"><rect x="0.5" y="0.5" width="12" height="12" rx="2" fill="#e9412e"/><rect x="3" y="4" width="7" height="5" fill="none" stroke="#fff" stroke-width="1"/><path d="M3 4 L6.5 7 L10 4" fill="none" stroke="#fff" stroke-width="1"/></svg>
        marcus@qvlearnix.com.au
      </li>
      <li class="contacts__item">
        <svg class="contacts__icon" viewBox="0 0 13 13"><rect x="0.5" y="0.5" width="12" height="12" rx="2" fill="#2fa36b"/><path d="M4 3 L6 3 L6 5 L5 6 C5.5 7.5 6 8 7 8 L8 7 L10 7 L10 9 C7 10.5 3 7 4 3 Z" fill="#fff"/></svg>
        0438157264
      </li>
      <li class="contacts__item">
        <svg class="contacts__icon" viewBox="0 0 13 13"><circle cx="6.5" cy="6.5" r="6" fill="#3f7fcf"/><circle cx="6.5" cy="6.5" r="3.5" fill="none" stroke="#fff" stroke-width="0.9"/><path d="M3 6.5 H10 M6.5 3 V10" stroke="#fff" stroke-width="0.9"/></svg>
        qvlearnix.com.au
      </li>
    </ul>

    <div class="brand-mark">
      <span class="brand-mark__dot"></span>QV Learnix Training
    </div>
  </section>

  <section class="card card--back" aria-label="Business card back">
    <div class="brand-mark">
      <span class="brand-mark__dot"></span>QV Learnix Training
    </div>

    <div class="services">
      <div class="services__item services__item--left">
        <p class="services__title">Strength &amp; Conditioning</p>
        <p>Training to peak your performance!</p>
      </div>
      <div class="services__item">
        <p class="services__title">Empowerment Coaching</p>
        <p>Harnessing your potential for success!</p>
      </div>
    </div>

    <div class="back-contacts">
      <span>0 438 157 264</span>
      <span>www.qvlearnix.com.au</span>
    </div>
  </section>

</main>
</body>
</html>
```